Bright and beautiful business card for a coach

I'm a personal and business coach based in Perth, Australia. I need a business card that whilst subtle and elegant, will stand out and appeal on a table full of cards.

My business name is Fern Coaching and the business card must represent the warmth and brightness implied in the name, without being gimmicky. It must have a warmth and appeal and be easy to read.

I prefer clean, minimalist designs.

It must align with the feel of my website and socials: https://www.ferncoachingplex.com.au/
https://www.instagram.com/ferncoachingplexau/
https://www.facebook.com/ferncoachingplexau
Updates

Deadline appearing 2 days away and still haven't completed brief - seems mighty short

Hi Designers Thank you so much for taking the time to submit designs. I wonder if I could have explained myself a little better. Most of the designs that have been submitted look rather formal and many have quite corporate looking embellishments on them (to my eye). I would like softer, warmer, more organic. I’m open to people playing about and being more abstract, using softer embellishments (e.g the line drawing flowers and grasses I’ve used in my socials) incorporating other colours from my palette or like the social icons in my email signature (in PDF), perhaps playing with size/oversize, playing with the bleed. Please don’t be constrained by what I’ve already done, it merely needs to compliment. I’m sorry if I’m not using the right words or have led you astray. I’m no designer, but I’ve done my website, socials, email signature etc all myself (my logo was a design contest) and I was really hoping for my business card to be something more creative than I could have made with a template. Reminder: No black cards/sides please. Thank you 😊

Target Market(s)

Individuals, most likely but not all female. Creative thinkers. Likely professionals.

Industry/Entity Type

Business & Personal Coach

Contact Information for Business Card

(Fern Coaching Logo) Name: Marla Pendry; Title: Business & Personal Coach; Phone number: +61 (0)498 315807; Email: marla@ferncoachingplex.com.au; Website: https://ferncoachingplex.com.au; Social icons for Facebook, Instagram & LinkedIn: @ferncoachingplexAU. Optional strapline: "A thinking partner to help you cut through the noise"

Font styles to use
Sans Serif

Colors
00AB8E
00BBA5
67D7C9
C6EFE9
E9F9F6
59FF00
82FF00
B8FF75
E3FFCB
F4FFEA
FFC000
F8CF3A
FAE287
FDF2CF
FEFAEE

Requirements
Must have
• Must align with feel of my website and socials. Must have a pop of #FFC000 (possibly whole of one side, or at least a block). Bright or white background. Easy to read.
Nice to have
• Possibly incorporate the sunshine/grass picture I have used in website and socials - will upload.
Should not have
• Must not be black or dark. Not impersonal or corporate looking.

```html
<!DOCTYPE html>
<html lang="en">
<head>
<meta charset="utf-8">
<title>Fern Coaching – Business Card</title>
<link rel="stylesheet" href="https://fonts.googleapis.com/css2?family=Lato:wght@300;400;700&display=swap">
<style>
  :root {
    --sun: #FFC000;
    --sun-soft: #F8CF3A;
    --ink: #2b2b2b;
    --grey: #8a8a8a;
    --rule: #9a9a9a;
    --paper: #fcfcfd;
    --stage: #eceeef;
    --grass-dark: #4f6a1c;
    --grass: #8fb23a;
    --glow: #f3c46a;
  }
  * { box-sizing: border-box; margin: 0; padding: 0; }
  html, body { width: 1200px; height: 1108px; overflow: hidden; }
  body {
    background: var(--stage);
    font-family: 'Lato', sans-serif;
    display: flex; align-items: center; justify-content: center; gap: 64px;
  }
  .card {
    width: 460px; height: 800px; border-radius: 28px; overflow: hidden;
    position: relative; box-shadow: 0 10px 30px rgba(0,0,0,.12);
  }
  /* Contact side */
  .card-contact {
    background: var(--paper);
    display: flex; flex-direction: column; align-items: center; text-align: center;
    padding-top: 170px;
  }
  .brand-name { font-size: 46px; font-weight: 300; color: var(--sun); letter-spacing: 1px; }
  .brand-sub { font-size: 20px; letter-spacing: 10px; color: var(--grey); margin-top: 10px; }
  .person-name { margin-top: 130px; font-size: 38px; font-weight: 300; color: var(--sun); }
  .person-title { font-size: 22px; color: var(--ink); margin-top: 6px; }
  .rule-row { display: flex; align-items: center; gap: 10px; width: 300px; margin-top: 22px; }
  .rule-row::before, .rule-row::after { content: ""; flex: 1; height: 1px; background: var(--rule); }
  .icon-tile { width: 32px; height: 32px; border-radius: 6px; background: var(--sun); display: flex; align-items: center; justify-content: center; }
  .icon-dot { width: 32px; height: 32px; border-radius: 50%; background: var(--sun); }
  .contact-list { list-style: none; font-size: 20px; color: var(--ink); line-height: 1.5; margin-top: 14px; }
  .contact-list .hl { color: var(--sun); }
  .handle { font-size: 20px; color: var(--ink); margin-top: 12px; }
  /* Message side */
  .card-message { background: var(--grass-dark); }
  .scene-photo {
    position: absolute; inset: 0;
    background:
      radial-gradient(circle at 88% 12%, #fff3cf 0%, var(--glow) 12%, rgba(210,140,60,.55) 28%, transparent 50%),
      linear-gradient(180deg, #6f7a3a 0%, var(--grass) 45%, #7aa22e 70%, var(--grass-dark) 100%);
  }
  .message-brand { position: absolute; top: 250px; left: 0; right: 0; text-align: center; color: #fff; }
  .message-brand .brand-name { color: #fff; }
  .message-brand .brand-sub { color: #fff; }
  .strap-band {
    position: absolute; left: 0; right: 0; top: 600px; height: 120px;
    background: var(--sun); display: flex; align-items: center; justify-content: center;
    color: #fff; font-size: 23px; text-transform: uppercase; text-align: center; line-height: 1.35; padding: 0 24px;
  }
</style>
</head>
<body>
  <section class="card card-contact">
    <div class="brand-name">Fern Coaching</div>
    <div class="brand-sub">COACHING</div>
    <div class="person-name">Marla Pendry</div>
    <div class="person-title">Business &amp; Personal Coach</div>
    <div class="rule-row">
      <span class="icon-tile"><svg width="18" height="18" viewBox="0 0 24 24"><path d="M6 3l4 1 1 4-2 2a12 12 0 006 6l2-2 4 1 1 4-2 2C10 21 3 14 4 5z" fill="#fff"/></svg></span>
      <span class="icon-tile"><svg width="18" height="18" viewBox="0 0 24 24"><rect x="3" y="6" width="18" height="12" fill="none" stroke="#fff" stroke-width="2"/><path d="M3 6l9 7 9-7" fill="none" stroke="#fff" stroke-width="2"/></svg></span>
      <span class="icon-tile"><svg width="18" height="18" viewBox="0 0 24 24"><circle cx="12" cy="12" r="8" fill="none" stroke="#fff" stroke-width="2"/><path d="M4 12h16M12 4c3 3 3 13 0 16M12 4c-3 3-3 13 0 16" fill="none" stroke="#fff" stroke-width="1.5"/></svg></span>
    </div>
    <ul class="contact-list">
      <li>+61 (0)498 315807</li>
      <li>marla@ferncoachingplex.com.au</li>
      <li>www.<span class="hl">ferncoachingplex</span>.com.au</li>
    </ul>
    <div class="rule-row">
      <span class="icon-dot"></span><span class="icon-dot"></span><span class="icon-dot"></span>
    </div>
    <div class="handle">@ferncoachingplexAU</div>
  </section>

  <section class="card card-message">
    <div class="scene-photo" role="img" aria-label="Close-up of green grass blades lit by warm morning sunlight"></div>
    <div class="message-brand">
      <div class="brand-name">Fern Coaching</div>
      <div class="brand-sub">COACHING</div>
    </div>
    <div class="strap-band">A thinking partner to help<br>you cut through the noise</div>
  </section>
</body>
</html>
```